Brannigan Ashcroft LLC. custom built/handcrafted

I am recent small business owner looking to sell my art(drawings) and woodworking projects from my home. I have a very rough draft of a simple card design created on a simple digital program. I was hoping for a fancier lettering on the initial letters (BA). More of a calligraphy style. Also, the yellow border around the logo I would like to be a gold foil look. For it to be shiny or reflective look and to keep the other letters black with a consistent font on the card and the card white.

Target Market(s)

Local and neighboring cities

Industry/Entity Type

Art (drawing)/Woodworking

Contact Information for Business Card

My email tpashcroft@mailvane.net, phone number 949-517-3068. In the files provided it has a yellow border around the logo and I was looking to make that a gold foil.

Font styles to use
Serif
Decorative
Script

Requirements
Nice to have
• symbols for having a Facebook and Instagram

```html
<!DOCTYPE html>
<html lang="en">
<head>
<meta charset="utf-8">
<title>Brannigan Ashcroft LLC. – Business Card</title>
<link rel="stylesheet" href="https://fonts.googleapis.com/css2?family=Marcellus&family=Alegreya+Sans:wght@400&display=swap">
<style>
  :root {
    --backdrop: #c9c9c9;
    --card-white: #ffffff;
    --gold: #cba32c;
    --ink: #111111;
  }
  * { margin: 0; padding: 0; box-sizing: border-box; }
  html, body {
    width: 1200px; height: 846px; overflow: hidden;
    background: var(--backdrop);
  }
  .canvas { position: relative; width: 1200px; height: 846px; }

  .card {
    position: absolute;
    left: 346px;
    width: 508px;
    height: 290px;
  }
  .card--front { top: 113px; background: var(--card-white); }
  .card--back  { top: 442px; background: var(--gold); }

  /* Front */
  .logo-frame {
    position: absolute;
    left: 51px; top: 34px;
    width: 407px; height: 198px;
    border: 2px solid var(--gold);
    display: flex; align-items: center; justify-content: center;
  }
  .logo-name {
    font-family: "Marcellus", serif;
    font-size: 27px;
    letter-spacing: 0.5px;
    color: var(--ink);
    white-space: nowrap;
  }
  .tagline {
    position: absolute;
    left: 0; right: 0; top: 245px;
    text-align: center;
    font-family: "Marcellus", serif;
    font-size: 22px;
    letter-spacing: 1px;
    color: var(--ink);
  }
  .tagline__dot {
    display: inline-block;
    width: 5px; height: 5px; border-radius: 50%;
    background: var(--ink);
    vertical-align: middle;
    margin: 0 8px 4px;
  }

  /* Back */
  .owner-name {
    position: absolute;
    left: 0; right: 0; top: 98px;
    text-align: center;
    font-family: "Marcellus", serif;
    font-size: 34px;
    letter-spacing: 0.5px;
    color: var(--ink);
  }
  .owner-role {
    position: absolute;
    left: 76px; right: 74px; top: 142px;
    display: flex; align-items: center; gap: 9px;
    font-family: "Marcellus", serif;
    font-size: 23px;
    color: var(--ink);
  }
  .owner-role__rule { flex: 1; height: 1px; background: var(--ink); }

  .contact-list {
    position: absolute;
    top: 192px;
    list-style: none;
    font-family: "Alegreya Sans", sans-serif;
    font-size: 16.5px;
    color: var(--ink);
  }
  .contact-list--left  { left: 32px; }
  .contact-list--right { left: 250px; }
  .contact-item {
    display: flex; align-items: center;
    height: 23px;
  }
  .contact-icon {
    width: 17px; height: 17px;
    margin-right: 6px;
    flex: none;
  }
  .contact-icon--square {
    background: var(--ink);
    border-radius: 2px;
  }
</style>
</head>
<body>
<main class="canvas">

  <section class="card card--front" aria-label="Card front">
    <div class="logo-frame">
      <span class="logo-name">BRANNIGAN ASHCROFT</span>
    </div>
    <p class="tagline">CUSTOM BUILT<span class="tagline__dot"></span>HANDCRAFTED</p>
  </section>

  <section class="card card--back" aria-label="Card back">
    <h1 class="owner-name">THOMAS P. ASHCROFT</h1>
    <div class="owner-role">
      <span class="owner-role__rule"></span>
      <span>OWNER</span>
      <span class="owner-role__rule"></span>
    </div>

    <ul class="contact-list contact-list--left">
      <li class="contact-item">
        <svg class="contact-icon" viewBox="0 0 24 24" aria-hidden="true">
          <path fill="currentColor" d="M9 1.5c-2.5 .8-4.5 3.5-4.5 8.5s2 10 4.8 12.5c.8.6 1.8.4 2.3-.3l1-1.7c.4-.7.2-1.5-.5-1.9l-1.8-1.1c-.6-.4-1.1-2.7-1.1-6.5s.5-6 1.1-6.5l1.8-1c.7-.4.9-1.2.5-1.9l-1-1.7C11 1.2 10 1 9 1.5z"/>
        </svg>
        <span>949-517-3068</span>
      </li>
      <li class="contact-item">
        <svg class="contact-icon" viewBox="0 0 24 24" aria-hidden="true">
          <rect x="1" y="5" width="22" height="14" fill="currentColor"/>
          <path d="M2 6l10 7 10-7M2 18l7-6M22 18l-7-6" stroke="#cba32c" stroke-width="1.4" fill="none"/>
        </svg>
        <span>tpashcroft@mailvane.net</span>
      </li>
    </ul>

    <ul class="contact-list contact-list--right">
      <li class="contact-item">
        <span class="contact-icon contact-icon--square" aria-hidden="true"></span>
        <span>tpashcroft@friendsquare.net</span>
      </li>
      <li class="contact-item">
        <span class="contact-icon contact-icon--square" aria-hidden="true"></span>
        <span>tpashcroft@photoloop.net</span>
      </li>
    </ul>
  </section>

</main>
</body>
</html>
```